Business card logo

Hello, I would like a business card for my law firm with a logo composed of my initials "CV". The logo is intended to appear on my business card, my letterhead, envelope and documents from my office. My first and last name (Camille Vautrin) and "Lawyer" must appear next to the logo. I would like the logo and the characters to be in golden color on a dark background (example black, navy blue). I would especially like a refined work on the logo which should be composed of the letters J and R.

```html
<!DOCTYPE html>
<html lang="en">
<head>
<meta charset="utf-8">
<title>Camille Vautrin — Lawyer business card</title>
<link href="https://fonts.googleapis.com/css2?family=Montserrat:wght@300;400;500&display=swap" rel="stylesheet">
<style>
  :root {
    --page-bg: #e9e6e1;
    --card-black: #141414;
    --card-black-light: #262626;
    --gold: #c9a466;
    --text-white: #f2f2f2;
    --text-grey: #bdbdbd;
  }
  * { margin: 0; padding: 0; box-sizing: border-box; }
  html, body {
    width: 1200px;
    height: 1022px;
    overflow: hidden;
    background: var(--page-bg);
  }
  .stage {
    width: 1200px;
    height: 1022px;
    display: flex;
    align-items: center;
    justify-content: center;
  }
  .business-card {
    position: relative;
    width: 900px;
    height: 514px;
    background: linear-gradient(135deg, var(--card-black-light) 0%, var(--card-black) 55%, #0d0d0d 100%);
    border-radius: 6px;
    box-shadow: 0 18px 40px rgba(0,0,0,0.28);
    display: flex;
    align-items: center;
  }
  .brand-block {
    width: 470px;
    display: flex;
    justify-content: center;
  }
  .brand-name {
    display: flex;
    align-items: center;
    gap: 14px;
    font-family: "Montserrat", sans-serif;
    font-weight: 500;
    font-size: 34px;
    line-height: 1;
    color: var(--gold);
    white-space: nowrap;
  }
  .brand-square {
    width: 16px;
    height: 16px;
    background: var(--gold);
    flex: none;
  }
  .divider {
    width: 2px;
    height: 240px;
    background: var(--gold);
  }
  .contact-block {
    padding-left: 46px;
    font-family: "Montserrat", sans-serif;
  }
  .contact-name {
    font-weight: 500;
    font-size: 28px;
    letter-spacing: 0.5px;
    color: var(--text-white);
    text-transform: uppercase;
  }
  .contact-role {
    font-weight: 400;
    font-size: 22px;
    color: var(--text-grey);
    margin-bottom: 22px;
  }
  .contact-list { list-style: none; }
  .contact-item {
    display: flex;
    align-items: center;
    gap: 14px;
    font-weight: 300;
    font-size: 24px;
    color: var(--text-white);
    margin-bottom: 10px;
    white-space: nowrap;
  }
  .contact-icon { width: 22px; height: 22px; flex: none; }
</style>
</head>
<body>
<main class="stage">
  <section class="business-card" aria-label="Business card front">
    <div class="brand-block">
      <div class="brand-name"><span class="brand-square"></span>Camille Vautrin</div>
    </div>
    <div class="divider"></div>
    <div class="contact-block">
      <div class="contact-name">Camille Vautrin</div>
      <div class="contact-role">Lawyer</div>
      <ul class="contact-list">
        <li class="contact-item">
          <svg class="contact-icon" viewBox="0 0 24 24" aria-hidden="true">
            <circle cx="12" cy="12" r="10" fill="none" stroke="#c9a466" stroke-width="2"/>
            <path d="M8.5 7.5l2 2-1 1.2c.7 1.5 1.8 2.6 3.3 3.3l1.2-1 2 2-1.3 1.5c-3.6-.6-6.6-3.6-7.2-7.2z" fill="#c9a466"/>
          </svg>
          514-207-3860
        </li>
        <li class="contact-item">
          <svg class="contact-icon" viewBox="0 0 24 24" aria-hidden="true">
            <rect x="3" y="6" width="18" height="12" fill="none" stroke="#c9a466" stroke-width="2"/>
            <path d="M3 6l9 7 9-7" fill="none" stroke="#c9a466" stroke-width="2"/>
          </svg>
          info@vautrinavocate.com
        </li>
        <li class="contact-item">
          <svg class="contact-icon" viewBox="0 0 24 24" aria-hidden="true">
            <circle cx="12" cy="12" r="10" fill="#c9a466"/>
            <path d="M2 12h20M12 2c3 3 3 17 0 20M12 2c-3 3-3 17 0 20" fill="none" stroke="#141414" stroke-width="1.4"/>
          </svg>
          www.vautrinavocate.com
        </li>
      </ul>
    </div>
  </section>
</main>
</body>
</html>
```